Consultants Need a Powerful New Image to Support a New Concept

We need a better image for an idea we have. Will be used in powerpoint but also in print (workbooks, handouts etc). The notion is that in any moment people in an organisation can choose to tell positive stories about what is going well, what they enjoy, what they are hopeful for or negative stories about what is wrong, not working or they are frustrated and pissed off about.

Target Market(s)

Leaders in organisations

Industry/Entity Type

It Support

Font styles to use
Sans Serif

Requirements
Must have
• The ability to build the image in powerpoint (at least add the text). Needs also to be used as a stand alone. Font and palette consistency with other materials. Some examples attached as well as font files and colour guidelines. Notice the left hand side of the model is about tell the stories and the right hand side is about how telling positive stories encourages others to seek more positive stories. On the right hand side down the bottom, the point is that these negative stories are so easy to join in on and they spread quickly and breed cynicism. Note the "Storyline" running up and down the middle - storyline model attached.
Nice to have
• A sense of momentum both up and down - the more positive stories we tell the more the organisation is energised and positive, the more negative stories (whingeing and complaining) the worse it is.

```html
<!DOCTYPE html>
<html lang="en">
<head>
<meta charset="utf-8">
<title>The Conversational Moment – Storyline Model</title>
<link rel="stylesheet" href="https://fonts.googleapis.com/css2?family=Arimo:ital,wght@0,400;0,700;1,700&family=Fredoka:wght@500;600&family=Cinzel:wght@900&display=swap">
<style>
  :root {
    --navy: #1f2547;
    --ink: #1b1d3c;
    --grey-text: #a3a3a3;
    --green-box: #6fa956;
    --dark-box: #4b4d6b;
    --green-head: #4f9a2c;
    --blue-orb: #1c3f86;
    --green-orb: #5cae2b;
    --ice: #bfe6f5;
    --spiral: #c4c4c4;
    --white: #ffffff;
  }
  * { margin: 0; padding: 0; box-sizing: border-box; }
  html, body { width: 1200px; height: 682px; overflow: hidden; background: var(--white); }
  .canvas { position: relative; width: 1200px; height: 682px; font-family: "Arimo", Arial, sans-serif; }
  .shapes { position: absolute; inset: 0; }

  .stage-box {
    position: absolute; width: 179px; border-radius: 10px;
    display: flex; align-items: center; justify-content: center; text-align: center;
    color: var(--white); font-family: "Fredoka", "Trebuchet MS", sans-serif; font-weight: 600;
    font-size: 17px; line-height: 1.45; letter-spacing: .3px; padding: 6px;
  }
  .stage-box--positive { background: var(--green-box); }
  .stage-box--negative { background: var(--dark-box); }

  .story-label { position: absolute; }
  .story-label__title { font-weight: 700; font-size: 27px; letter-spacing: .3px; line-height: 1.1; }
  .story-label__note { font-style: italic; font-weight: 700; font-size: 21px; color: var(--grey-text); line-height: 1.35; }
  .story-label--right-aligned { text-align: right; }
  .story-label--positive .story-label__title { color: var(--ink); }
  .story-label--negative .story-label__title { color: var(--green-head); }

  .moment-caption {
    position: absolute; left: 945px; top: 285px; width: 235px; text-align: center;
    font-style: italic; font-size: 31px; line-height: 1.22; color: var(--ink);
  }
  .orb-label { font-family: "Cinzel", Georgia, serif; font-weight: 900; font-size: 21px; fill: var(--white); }
  .question-mark { font-family: "Arimo", Arial, sans-serif; font-weight: 700; font-size: 54px; fill: var(--blue-orb); }

  .brand { position: absolute; left: 6px; top: 630px; display: flex; align-items: center; gap: 10px; }
  .brand__dot { width: 36px; height: 36px; border-radius: 50%; background: var(--navy); }
  .brand__name { font-size: 36px; font-weight: 400; color: var(--navy); }
</style>
</head>
<body>
<div class="canvas">
  <svg class="shapes" width="1200" height="682" viewBox="0 0 1200 682" aria-hidden="true">
    <defs>
      <linearGradient id="iceLeft" x1="0" x2="1">
        <stop offset="0" stop-color="#ffffff"/><stop offset="1" stop-color="#9fd9ef"/>
      </linearGradient>
      <linearGradient id="iceRight" x1="1" x2="0">
        <stop offset="0" stop-color="#ffffff"/><stop offset="1" stop-color="#9fd9ef"/>
      </linearGradient>
      <linearGradient id="goldArrow" x1="0" x2="1">
        <stop offset="0" stop-color="#5c4a33"/><stop offset="1" stop-color="#f4b71a"/>
      </linearGradient>
      <linearGradient id="blueCurve" x1="0" y1="0" x2="0" y2="1">
        <stop offset="0" stop-color="#2a64b8"/><stop offset="1" stop-color="#1b2b5a"/>
      </linearGradient>
      <linearGradient id="greenCurve" x1="0" y1="1" x2="0" y2="0">
        <stop offset="0" stop-color="#8bd12a"/><stop offset="1" stop-color="#3f8f1c"/>
      </linearGradient>
      <radialGradient id="orbBlue" cx=".4" cy=".3" r=".75">
        <stop offset="0" stop-color="#4f7fd0"/><stop offset=".6" stop-color="#1c3f86"/><stop offset="1" stop-color="#0d1f4a"/>
      </radialGradient>
      <radialGradient id="orbGreen" cx=".4" cy=".3" r=".75">
        <stop offset="0" stop-color="#b4e86a"/><stop offset=".6" stop-color="#5cae2b"/><stop offset="1" stop-color="#2f6d12"/>
      </radialGradient>
    </defs>

    <!-- storyline spiral -->
    <path d="M580 8 C700 22 700 55 592 70 C480 86 480 120 592 134 C700 150 700 184 592 200 C480 216 480 250 592 266 C700 282 700 316 592 340 C480 364 480 392 592 410 C700 428 700 462 592 480 C480 498 480 534 592 552 C700 570 700 606 592 622 C520 634 540 668 600 678"
          fill="none" stroke="var(--spiral)" stroke-width="26" opacity=".75"/>

    <!-- converging ice arrows -->
    <path d="M335 290 L470 300 L468 275 L540 340 L468 405 L470 380 L335 390 L372 340 Z" fill="url(#iceLeft)"/>
    <path d="M850 290 L715 300 L717 275 L645 340 L717 405 L715 380 L850 390 L813 340 Z" fill="url(#iceRight)"/>

    <!-- curved story arrows -->
    <path d="M283 188 Q313 242 345 268 L330 282 L382 297 L372 246 L360 258 Q337 225 324 182 Z" fill="url(#blueCurve)"/>
    <path d="M902 188 Q872 242 840 268 L855 282 L803 297 L813 246 L825 258 Q848 225 861 182 Z" fill="url(#blueCurve)"/>
    <path d="M281 500 Q303 430 340 398 L327 386 L382 383 L370 432 L359 418 Q336 446 321 502 Z" fill="url(#greenCurve)"/>
    <path d="M904 500 Q882 430 845 398 L858 386 L803 383 L815 432 L826 418 Q849 446 864 502 Z" fill="url(#greenCurve)"/>

    <!-- conversational moment arrow -->
    <path d="M962 318 L876 318 L876 306 L835 340 L876 374 L876 362 L962 362 Z" fill="url(#goldArrow)"/>

    <!-- moment cube -->
    <rect x="545" y="298" width="92" height="92" fill="var(--ice)" opacity=".55" stroke="#ffffff" stroke-width="2"/>
    <path d="M545 298 L560 284 L652 284 L637 298 Z" fill="#dff3fb" opacity=".8"/>
    <path d="M637 298 L652 284 L652 376 L637 390 Z" fill="#a9dcef" opacity=".7"/>
    <text class="question-mark" x="591" y="364" text-anchor="middle">?</text>

    <!-- storyline orbs -->
    <g>
      <circle cx="592" cy="55" r="34" fill="url(#orbBlue)" stroke="#0e1a3a" stroke-width="2"/>
      <text class="orb-label" x="592" y="63" text-anchor="middle">GET</text>
      <circle cx="592" cy="126" r="34" fill="url(#orbGreen)" stroke="#2b5d12" stroke-width="2"/>
      <text class="orb-label" x="592" y="134" text-anchor="middle">DO</text>
      <circle cx="592" cy="197" r="34" fill="url(#orbBlue)" stroke="#0e1a3a" stroke-width="2"/>
      <text class="orb-label" x="592" y="205" text-anchor="middle">BE</text>
      <circle cx="592" cy="269" r="34" fill="url(#orbGreen)" stroke="#2b5d12" stroke-width="2"/>
      <text class="orb-label" x="592" y="277" text-anchor="middle">SEE</text>

      <circle cx="592" cy="415" r="34" fill="url(#orbBlue)" stroke="#0e1a3a" stroke-width="2"/>
      <text class="orb-label" x="592" y="423" text-anchor="middle">SEE</text>
      <circle cx="592" cy="486" r="34" fill="url(#orbGreen)" stroke="#2b5d12" stroke-width="2"/>
      <text class="orb-label" x="592" y="494" text-anchor="middle">BE</text>
      <circle cx="592" cy="558" r="34" fill="url(#orbBlue)" stroke="#0e1a3a" stroke-width="2"/>
      <text class="orb-label" x="592" y="566" text-anchor="middle">DO</text>
      <circle cx="592" cy="630" r="34" fill="url(#orbGreen)" stroke="#2b5d12" stroke-width="2"/>
      <text class="orb-label" x="592" y="638" text-anchor="middle">GET</text>
    </g>
  </svg>

  <!-- positive storyline -->
  <div class="stage-box stage-box--positive" style="left:630px;top:2px;height:86px;">Fuels<br>UNHELPFUL<br>Beliefs</div>
  <div class="stage-box stage-box--positive" style="left:374px;top:77px;height:87px;">ENCOURAGES<br>Proactive<br>Behaviour</div>
  <div class="stage-box stage-box--positive" style="left:630px;top:94px;height:87px;">DESTROYS<br>Confidence</div>
  <div class="stage-box stage-box--positive" style="left:374px;top:170px;height:86px;">GIVES Insight,<br>Shapes Beliefs</div>
  <div class="stage-box stage-box--positive" style="left:630px;top:187px;height:87px;">UNDERMINES<br>Performance</div>

  <!-- negative storyline -->
  <div class="stage-box stage-box--negative" style="left:374px;top:407px;height:86px;">Fuels<br>UNHELPFUL<br>Beliefs</div>
  <div class="stage-box stage-box--negative" style="left:630px;top:440px;height:86px;">Builds<br>NEGATIVE<br>Energy</div>
  <div class="stage-box stage-box--negative" style="left:374px;top:501px;height:86px;">DESTROYS<br>Confidence</div>
  <div class="stage-box stage-box--negative" style="left:630px;top:533px;height:87px;">DISCOURAGES<br>Effort and<br>Action</div>
  <div class="stage-box stage-box--negative" style="left:374px;top:594px;height:85px;">UNDERMINES<br>Performance</div>

  <!-- story labels -->
  <div class="story-label story-label--positive story-label--right-aligned" style="right:889px;top:110px;">
    <div class="story-label__title">TELL STORIES:</div>
    <div class="story-label__note">Bright Spots &amp;<br>Possibility</div>
  </div>
  <div class="story-label story-label--positive" style="left:873px;top:114px;">
    <div class="story-label__title">SEEK STORIES:</div>
    <div class="story-label__note">Catch People Doing<br>Things Right</div>
  </div>
  <div class="story-label story-label--negative story-label--right-aligned" style="right:889px;top:479px;">
    <div class="story-label__title">TELL STORIES:</div>
    <div class="story-label__note">Complaint &amp; Failure</div>
  </div>
  <div class="story-label story-label--negative" style="left:869px;top:479px;">
    <div class="story-label__title">JOIN STORIES:</div>
    <div class="story-label__note">Cynicism, Sarcasm &amp;<br>Negativity</div>
  </div>

  <div class="moment-caption">The<br>Conversational<br>moment</div>

  <div class="brand">
    <span class="brand__dot"></span>
    <span class="brand__name">Kestrel</span>
  </div>
</div>
</body>
</html>
```